Business Card and Logo Color Scheme Design Contest

We are starting a new company called Lonestar Precision Surveying and already have a logo however, the colors for the logo itself are not final and COULD be changed. I'm hoping to move AWAYfrom the gold color in the card and the logo as it seems a bit outdated. What we need help with is to find what our business color scheme will be, and then incorporate those colors into both the logo and the business card design itself. We also want to make sure we are known as "LPS" so in the future we can just refer to ourselves as "LPS" and not Lonestar Precision Surveying. That being said, I would like to make a slight change to the logo to somehow include the letters "LPS." The logo used in the front of the card design MUST ALSO include the words "Firm No. 64307" within the logo. My vision is for the front of the card to have the information shown in the attached image. For the back of the card, I'm hoping to have something very simple. I'm envisioning a solid color with either the website (www.surveyplainsco.com) and a simplified version of the logo. I've attached an example but I'm looking for a complete redesign. I'm looking for a slick, modern and simple design.

Industry/Entity Type

Civil Engineer

Contact Information for Business Card

Logo
Firm No. 64307
Marcus Holloway, PE
Chief Operating Officer
Email:mholloway@surveyplainsco.com
Ph: 936.482.3095 | D: 936.482.3067 | M:210.347.6152
4718 W. Bramwell, Conroe, Texas 77318
www.surveyplainsco.com

Requirements
Must have
• Logo
Contact Info
Nice to have
• "LPS" Incorporated in the design
Should not have
• The current color scheme

```html
<!DOCTYPE html>
<html lang="en">
<head>
<meta charset="utf-8">
<title>Lonestar Precision Surveying – Business Card</title>
<link href="https://fonts.googleapis.com/css2?family=Montserrat:wght@500;700&family=Arimo:wght@400&display=swap" rel="stylesheet">
<style>
  :root {
    --red: #c4161c;
    --ink: #1c1c1c;
    --paper: #ffffff;
    --charcoal: #2a2a2a;
    --pattern: #333333;
    --rule: #c9c9c9;
    --backdrop: #e6e6e6;
  }
  * { margin: 0; padding: 0; box-sizing: border-box; }
  html, body { width: 1200px; height: 1015px; overflow: hidden; }
  body {
    background: var(--backdrop);
    position: relative;
    font-family: "Arimo", Arial, sans-serif;
    color: var(--ink);
  }
  .card {
    position: absolute;
    width: 620px;
    height: 354px;
    box-shadow: 0 10px 24px rgba(0,0,0,.25);
  }
  /* Back */
  .card-back {
    left: 90px; top: 100px;
    background: var(--charcoal);
  }
  .card-back .pattern {
    position: absolute; inset: 0;
    background: linear-gradient(135deg, var(--pattern), var(--charcoal) 70%);
  }
  .card-back .mark {
    position: absolute;
    left: 420px; top: 150px;
    display: flex; align-items: center; gap: 8px;
    font-family: "Montserrat", sans-serif;
    font-weight: 700;
    font-size: 30px;
    letter-spacing: 2px;
    color: var(--paper);
  }
  .card-back .mark .dot {
    width: 8px; height: 8px; background: var(--red);
  }
  /* Front */
  .card-front {
    left: 490px; top: 560px;
    background: var(--paper);
  }
  .brand {
    position: absolute;
    left: 34px; top: 110px;
    width: 230px;
    text-align: center;
  }
  .brand .square {
    width: 18px; height: 18px;
    background: var(--red);
    margin: 0 auto 16px;
  }
  .brand .firm-name {
    font-family: "Montserrat", sans-serif;
    font-weight: 700;
    font-size: 19px;
    line-height: 1.2;
    color: var(--red);
    text-transform: uppercase;
  }
  .brand .firm-no {
    display: flex; align-items: center; gap: 10px;
    margin-top: 12px;
    font-family: "Montserrat", sans-serif;
    font-weight: 500;
    font-size: 11px;
    color: var(--ink);
  }
  .brand .firm-no::before, .brand .firm-no::after {
    content: ""; flex: 1; height: 1px; background: var(--ink);
  }
  .divider {
    position: absolute;
    left: 290px; top: 50px;
    width: 1px; height: 250px;
    background: var(--rule);
  }
  .contact {
    position: absolute;
    left: 318px; top: 52px;
    font-size: 14px;
    line-height: 1.3;
  }
  .contact .person {
    font-family: "Montserrat", sans-serif;
    font-weight: 700;
    font-size: 19px;
    color: var(--red);
    text-transform: uppercase;
  }
  .contact .role { margin-bottom: 14px; }
  .contact .address { margin-bottom: 12px; }
  .contact ul { list-style: none; }
  .contact li { display: flex; align-items: center; gap: 9px; }
  .contact li svg { width: 13px; height: 13px; flex: none; fill: var(--red); }
  .contact .accent { color: var(--red); }
</style>
</head>
<body>

<section class="card card-back">
  <div class="pattern" role="img" aria-label="Faint repeating brand-mark pattern across the dark card back"></div>
  <div class="mark"><span>LPS</span><span class="dot"></span></div>
</section>

<section class="card card-front">
  <div class="brand">
    <div class="square"></div>
    <div class="firm-name">Lonestar Precision Surveying</div>
    <div class="firm-no">Firm No. 64307</div>
  </div>

  <div class="divider"></div>

  <div class="contact">
    <div class="person">Marcus Holloway, PE</div>
    <div class="role">Chief Operating Officer</div>
    <div class="address">4718 W. Bramwell , Conroe<br>Texas 77318</div>
    <ul>
      <li><svg viewBox="0 0 16 16"><path d="M3 1l3 3-2 2c1 2 4 5 6 6l2-2 3 3-2 2C7 15 1 9 1 3z"/></svg>936.482.3095</li>
      <li><svg viewBox="0 0 16 16"><path d="M3 1l3 3-2 2c1 2 4 5 6 6l2-2 3 3-2 2C7 15 1 9 1 3z"/></svg>936.482.3067 <span class="accent">(Direct)</span></li>
      <li><svg viewBox="0 0 16 16"><path d="M4 0h8a1 1 0 011 1v14a1 1 0 01-1 1H4a1 1 0 01-1-1V1a1 1 0 011-1zm1 2v10h6V2z"/></svg>210.347.6152</li>
      <li><svg viewBox="0 0 16 16"><path d="M0 3h16v2L8 10 0 5zm0 4l8 5 8-5v6H0z"/></svg>mholloway@surveyplainsco.com</li>
      <li><svg viewBox="0 0 16 16"><path d="M8 0a8 8 0 100 16A8 8 0 008 0zm0 2c1 1 2 3 2 5H6c0-2 1-4 2-5zM6 9h4c0 2-1 4-2 5-1-1-2-3-2-5zM2 7c.3-2 1.6-3.7 3.4-4.5C4.6 3.9 4.1 5.4 4 7zm0 2h2c.1 1.6.6 3.1 1.4 4.5C3.6 12.7 2.3 11 2 9zm10-2c-.1-1.6-.6-3.1-1.4-4.5C12.4 3.3 13.7 5 14 7zm0 2h2c-.3 2-1.6 3.7-3.4 4.5.8-1.4 1.3-2.9 1.4-4.5z"/></svg>www.<span class="accent">surveyplainsco</span>.com</li>
    </ul>
  </div>
</section>

</body>
</html>
```